Icons for Buttons of Time Clock Kiosk

Create Icons for 6 buttons of a screen of a computer screen used by employees to record their work.
In the icons I am looking for different icon for each button.
The icon should contain an image that will be associated with its action.
For example "Start lunch" will have food.
The kiosks are used in agriculture mainly in packing houses.
An employee clicks those buttons when he starts the work day,
leave for break,
returns from break,
leaves for lunch,
returns from lunch,
and finishes the work day.
Agricultural Packing Facilities
Agriculture

```html
<!DOCTYPE html>
<html lang="en">
<head>
<meta charset="utf-8">
<title>Time Clock Kiosk</title>
<link rel="stylesheet" href="https://fonts.googleapis.com/css2?family=Source+Sans+3:wght@600&display=swap">
<style>
  :root {
    --page-bg: #d6d6d6;
    --screen-bg: #ffffff;
    --frame: #f5a83a;
    --header-bg: #5bc9e8;
    --header-ink: #1c1c1c;
    --green-light: #6fc487;
    --green-dark: #5ab56e;
    --orange-light: #f7a35f;
    --orange-dark: #e57f36;
    --blue-light: #3a55a4;
    --blue-dark: #213f83;
    --red-light: #f05a45;
    --red-dark: #e03c30;
    --purple-light: #882a85;
    --purple-dark: #652263;
    --yellow-light: #f2ef7e;
    --yellow-dark: #cdc352;
    --ink-light: #ffffff;
    --ink-dark: #1a1a1a;
  }
  * { box-sizing: border-box; margin: 0; padding: 0; }
  html, body {
    width: 1200px; height: 834px; overflow: hidden;
    background: var(--page-bg);
    font-family: "Source Sans 3", "Myriad Pro", sans-serif;
  }
  .kiosk-screen {
    position: absolute; left: 96px; top: 146px;
    width: 1009px; height: 544px;
    background: var(--screen-bg);
  }
  .kiosk-frame {
    position: absolute; left: 7px; top: 8px;
    width: 993px; height: 524px;
    border: 2.5px solid var(--frame);
  }
  .clock-bar {
    height: 35px; background: var(--header-bg);
    color: var(--header-ink);
    font-size: 21px; font-weight: 600; letter-spacing: 0.3px;
    display: flex; align-items: center; justify-content: center;
    word-spacing: 4px;
  }
  .punch-button {
    position: absolute; width: 250px; height: 103px;
    border-radius: 26px; overflow: hidden;
    background: var(--light);
    color: var(--ink);
  }
  .punch-button::before {
    content: ""; position: absolute; inset: 0;
    background: var(--dark);
    clip-path: polygon(142px 0, 100% 0, 100% 100%, 97px 100%);
  }
  .punch-label {
    position: absolute; left: 0; top: 0; width: 166px; height: 100%;
    display: flex; align-items: center; justify-content: center;
    font-size: 21px; font-weight: 600; white-space: nowrap;
  }
  .punch-icon {
    position: absolute; left: 157px; top: 17px; width: 68px; height: 68px;
  }
  .punch-icon .cycle,
  .punch-icon .glyph { fill: none; stroke: var(--ink); stroke-linecap: round; stroke-linejoin: round; }
  .punch-icon .cycle { stroke-width: 3; }
  .punch-icon .glyph { stroke-width: 2.2; }
  .punch-icon .solid { fill: var(--ink); stroke: none; }

  .col-left { left: 25px; }
  .col-right { left: 716px; }
  .row-1 { top: 140px; }
  .row-2 { top: 265px; }
  .row-3 { top: 388px; }

  .time-in { --light: var(--green-light); --dark: var(--green-dark); --ink: var(--ink-light); }
  .start-break { --light: var(--orange-light); --dark: var(--orange-dark); --ink: var(--ink-light); }
  .start-lunch { --light: var(--blue-light); --dark: var(--blue-dark); --ink: var(--ink-light); }
  .time-out { --light: var(--red-light); --dark: var(--red-dark); --ink: var(--ink-light); }
  .end-break { --light: var(--purple-light); --dark: var(--purple-dark); --ink: var(--ink-light); }
  .end-lunch { --light: var(--yellow-light); --dark: var(--yellow-dark); --ink: var(--ink-dark); }
</style>
</head>
<body>
  <main class="kiosk-screen">
    <div class="kiosk-frame">
      <header class="clock-bar">11/10/2021 10:18 AM</header>

      <div class="punch-button time-in col-left row-1">
        <span class="punch-label">Time IN</span>
        <svg class="punch-icon" viewBox="0 0 68 68" role="img" aria-label="Group of workers">
          <path class="cycle" d="M8 44 A28 28 0 0 1 47 9 M41 5 L47.5 9 L42 13.5 M60 24 A28 28 0 0 1 21 59 M27 63 L20.5 59 L26 54.5"/>
          <circle class="glyph" cx="23" cy="25" r="3.5"/>
          <circle class="glyph" cx="45" cy="25" r="3.5"/>
          <circle class="glyph" cx="34" cy="31" r="4"/>
          <path class="glyph" d="M17 37 a6 6 0 0 1 11 -3 M51 37 a6 6 0 0 0 -11 -3 M26 45 a8 8 0 0 1 16 0"/>
        </svg>
      </div>

      <div class="punch-button start-break col-left row-2">
        <span class="punch-label">Start Break</span>
        <svg class="punch-icon" viewBox="0 0 68 68" role="img" aria-label="Whistle">
          <path class="cycle" d="M8 44 A28 28 0 0 1 47 9 M41 5 L47.5 9 L42 13.5 M60 24 A28 28 0 0 1 21 59 M27 63 L20.5 59 L26 54.5"/>
          <path class="glyph" d="M29 31 H48 V38 H38 A8.5 8.5 0 1 1 29 31 Z"/>
          <circle class="glyph" cx="29" cy="39.5" r="3"/>
          <path class="glyph" d="M33 25 L31 19 M37 24 L37.5 18 M41 25 L44 20"/>
        </svg>
      </div>

      <div class="punch-button start-lunch col-left row-3">
        <span class="punch-label">Start lunch</span>
        <svg class="punch-icon" viewBox="0 0 68 68" role="img" aria-label="Worker seated at a table">
          <path class="cycle" d="M8 44 A28 28 0 0 1 47 9 M41 5 L47.5 9 L42 13.5 M60 24 A28 28 0 0 1 21 59 M27 63 L20.5 59 L26 54.5"/>
          <circle class="solid" cx="40" cy="19" r="3.5"/>
          <path class="glyph" d="M39 25 L37 37 H44 V47 M39 28 L32 32 M46 24 V42"/>
          <path class="glyph" d="M18 34 H34 M26 34 V47 M22 47 H30"/>
        </svg>
      </div>

      <div class="punch-button time-out col-right row-1">
        <span class="punch-label">Time OUT</span>
        <svg class="punch-icon" viewBox="0 0 68 68" role="img" aria-label="Open hand waving goodbye">
          <path class="cycle" d="M8 44 A28 28 0 0 1 47 9 M41 5 L47.5 9 L42 13.5 M60 24 A28 28 0 0 1 21 59 M27 63 L20.5 59 L26 54.5"/>
          <path class="glyph" d="M26 35 V23 M31 33 V19 M36 33 V20 M41 35 V24 M26 35 V40 Q26 48 34 48 Q41 48 43 41 L47 33"/>
        </svg>
      </div>

      <div class="punch-button end-break col-right row-2">
        <span class="punch-label">End Break</span>
        <svg class="punch-icon" viewBox="0 0 68 68" role="img" aria-label="Ringing bell">
          <path class="cycle" d="M8 44 A28 28 0 0 1 47 9 M41 5 L47.5 9 L42 13.5 M60 24 A28 28 0 0 1 21 59 M27 63 L20.5 59 L26 54.5"/>
          <path class="glyph" d="M23 42 H45 M27 42 V33 A7 7 0 0 1 41 33 V42 M34 26 V23"/>
          <circle class="solid" cx="34" cy="46" r="2.2"/>
          <path class="glyph" d="M20 30 Q19 26 22 23 M48 30 Q49 26 46 23"/>
        </svg>
      </div>

      <div class="punch-button end-lunch col-right row-3">
        <span class="punch-label">End Lunch</span>
        <svg class="punch-icon" viewBox="0 0 68 68" role="img" aria-label="Crossed fork and knife">
          <path class="cycle" d="M8 44 A28 28 0 0 1 47 9 M41 5 L47.5 9 L42 13.5 M60 24 A28 28 0 0 1 21 59 M27 63 L20.5 59 L26 54.5"/>
          <path class="glyph" d="M21 20 Q31 24 35 33 L31 35 Z M33 34 L46 47"/>
          <path class="glyph" d="M23 47 L41 29 M38 26 L44 32 M38 26 L43 21 M41 29 L46 24 M44 32 L49 27"/>
        </svg>
      </div>
    </div>
  </main>
</body>
</html>
```